Keystone Haulers Billboard design

I need two billboard designs using our logo and adding a few words Looking for a black background with our logo and wording in either purple or white.

need it to have our website keystonehaulers-example.com. phone number 555 201 4387

Also have 16/20/30 yard dumpsters available!

one billboard is size 7x21 feet the other is 15x 21 ft

Target Market(s)

Contractors, home owners

Requirements
Must have
• Use font similar to logo that is eye catching

```html
<!DOCTYPE html>
<html lang="en">
<head>
<meta charset="utf-8">
<title>Keystone Haulers Billboards</title>
<link rel="stylesheet" href="https://fonts.googleapis.com/css2?family=Montserrat:wght@700;800&display=swap">
<style>
  :root {
    --page: #ffffff;
    --black: #151515;
    --charcoal: #222222;
    --purple-deep: #4a2a5e;
    --purple: #7b3f98;
    --white: #ffffff;
    --photo-tone: #5a5560;
  }
  * { margin: 0; padding: 0; box-sizing: border-box; }
  html, body { width: 707px; height: 1200px; overflow: hidden; background: var(--page); }
  body { position: relative; font-family: "Montserrat", Arial, sans-serif; color: var(--white); }

  .billboard { position: absolute; left: 55px; width: 593px; overflow: hidden; }

  /* 7 x 21 ft */
  .billboard--wide {
    top: 54px; height: 198px;
    background: linear-gradient(to bottom, var(--black) 0%, #1c1a1f 45%, var(--purple-deep) 78%, var(--purple) 100%);
  }
  .billboard--wide .truck-photo {
    position: absolute; inset: 0;
    background: linear-gradient(to right, rgba(90,85,96,.55) 0%, rgba(90,85,96,.15) 30%, rgba(0,0,0,0) 50%, rgba(90,85,96,.15) 70%, rgba(90,85,96,.55) 100%);
  }
  .billboard--wide .brand-name {
    position: absolute; top: 72px; left: 0; right: 0; text-align: center;
    font-size: 40px; font-weight: 800; letter-spacing: 1px; line-height: 1;
  }
  .billboard--wide .tagline {
    position: absolute; top: 131px; left: 0; right: 0; text-align: center;
    font-size: 21px; font-weight: 700; letter-spacing: .3px;
  }
  .billboard--wide .contact {
    position: absolute; top: 172px; left: 0; right: 0;
    display: flex; justify-content: center; gap: 16px;
    font-size: 11.5px; font-weight: 700;
  }

  /* 15 x 21 ft */
  .billboard--tall {
    top: 309px; height: 830px;
    background: linear-gradient(to bottom, var(--charcoal) 0%, #1a1a1a 30%, #1c1a1e 55%, var(--purple-deep) 78%, var(--purple) 100%);
  }
  .billboard--tall .brand-name {
    position: absolute; top: 110px; left: 0; right: 0; text-align: center;
    font-size: 58px; font-weight: 800; line-height: 1.05; letter-spacing: 1px;
  }
  .billboard--tall .truck-photo {
    position: absolute; left: 45px; top: 236px; width: 512px; height: 310px;
    background: radial-gradient(ellipse at 45% 60%, #d8d8dc 0%, #8a8890 40%, rgba(40,38,44,0) 72%);
  }
  .billboard--tall .tagline {
    position: absolute; top: 582px; left: 0; right: 0; text-align: center;
    font-size: 40px; font-weight: 700; line-height: 1.25;
  }
  .billboard--tall .contact {
    position: absolute; top: 733px; left: 0; right: 0;
    display: flex; flex-direction: column; align-items: center; gap: 6px;
    font-size: 28px; font-weight: 700;
  }

  .contact-item { display: flex; align-items: center; gap: 6px; }
  .icon { flex: none; }
  .billboard--wide .icon { width: 15px; height: 15px; }
  .billboard--tall .icon { width: 26px; height: 26px; margin-right: 6px; }
</style>
</head>
<body>

<section class="billboard billboard--wide">
  <div class="truck-photo" role="img" aria-label="Roll-off dumpster trucks flanking the logo, faded into the dark background"></div>
  <h1 class="brand-name">KEYSTONE HAULERS</h1>
  <p class="tagline">PROVIDE 16/20/30 YARD TRASH BINS</p>
  <div class="contact">
    <span class="contact-item">
      <svg class="icon" viewBox="0 0 24 24" fill="none" stroke="currentColor" stroke-width="1.5"><circle cx="12" cy="12" r="11"/><circle cx="12" cy="12" r="7"/><ellipse cx="12" cy="12" rx="3" ry="7"/><path d="M5 12h14M6 9h12M6 15h12"/></svg>
      KEYSTONEHAULERS-EXAMPLE.COM
    </span>
    <span class="contact-item">
      <svg class="icon" viewBox="0 0 24 24" fill="none" stroke="currentColor" stroke-width="1.5"><circle cx="12" cy="12" r="11"/><path d="M8 7.5c-.8.8-.6 2.8 1.5 5.2 2.3 2.5 4.6 3.2 5.5 2.3l.8-.8-2.2-1.8-1 .8c-.8-.3-2.2-1.6-2.6-2.6l.8-1-1.8-2.2z"/></svg>
      555 201 4387
    </span>
  </div>
</section>

<section class="billboard billboard--tall">
  <h1 class="brand-name">KEYSTONE<br>HAULERS</h1>
  <div class="truck-photo" role="img" aria-label="White roll-off dumpster truck with raised black hoist, side view"></div>
  <p class="tagline">PROVIDE 16/20/30 YARD<br>TRASH BINS</p>
  <div class="contact">
    <span class="contact-item">
      <svg class="icon" viewBox="0 0 24 24" fill="none" stroke="currentColor" stroke-width="1.5"><circle cx="12" cy="12" r="11"/><circle cx="12" cy="12" r="7"/><ellipse cx="12" cy="12" rx="3" ry="7"/><path d="M5 12h14M6 9h12M6 15h12"/></svg>
      KEYSTONEHAULERS-EXAMPLE.COM
    </span>
    <span class="contact-item">
      <svg class="icon" viewBox="0 0 24 24" fill="none" stroke="currentColor" stroke-width="1.5"><circle cx="12" cy="12" r="11"/><path d="M8 7.5c-.8.8-.6 2.8 1.5 5.2 2.3 2.5 4.6 3.2 5.5 2.3l.8-.8-2.2-1.8-1 .8c-.8-.3-2.2-1.6-2.6-2.6l.8-1-1.8-2.2z"/></svg>
      555 201 4387
    </span>
  </div>
</section>

</body>
</html>
```